Wordpress website design needed for website re-launch of established lawn care company (Design mu...

We are a gardening company and are separating and re-launching the lawn care part of the company. We already have a non-wordpress website which includes a lawn care section and therefore contains all the content needed for the new website. We essentially need to take that content (over 6 pages) and re-create it into a new, modern and visually appealing design in our new Wordpress website. We use Veko and therefore the new design must be built and be compatible with the Veko theme. However, I am not looking to use a pre-built Veko layout or any template offered by Marrow Studio. I could easily do that myself. I'm looking for a bespoke design.

The pages of our current website that need to be re-designed within Veko are:
http://www.brambleworth.co.uk/lawncare/4593693096
http://www.brambleworth.co.uk/lawnfertilisers/4593712410
http://www.brambleworth.co.uk/lawnaeration/4593746736
http://www.brambleworth.co.uk/lawnscarification/4593747084
http://www.brambleworth.co.uk/lawntreatments/4593757226
http://www.brambleworth.co.uk/lawncarepackages/4593712492

Our Wordpress site is already set up with Hostara with the domain www.brambleworthlawns.co.uk and as I say, uses the Veko theme. I am not sure how you will deliver your designs but it must be using or compatible with Veko.

Target Market(s)

Homeowners ages 30+

Industry/Entity Type

Gardener

Font styles to use
Sans Serif

Colors
a64599
9bcb3c

Requirements
Must have
• The new site must still use our existing company colours - purple and green. Have a look on www.brambleworth.co.uk to get the right colours.
• Must be mobile responsive
Nice to have
• We want a fresh and modern new look for our new lawn care website.
• I have also attached a picture of our van and lawn care flyers so you can see what our current branding and style looks like in case it helps with your design.
Should not have
• Please don't just submit pre-designed templates that bear no relevance to my brief or requirements above. I could very easily go and install a pre-designed template and plug my content in but that's not what I'm looking for. Submissions should take into consideration my existing content, my brand colours and my logo as a minimum.

```html
<!DOCTYPE html>
<html lang="en">
<head>
<meta charset="utf-8">
<title>Brambleworth Lawn Care Services</title>
<link href="https://fonts.googleapis.com/css2?family=Cinzel:wght@400;700&family=Oswald:wght@400;500&family=Open+Sans:wght@400;600&display=swap" rel="stylesheet">
<style>
:root{
  --purple:#a64599;
  --green:#9bcb3c;
  --green-dark:#5f8f1f;
  --charcoal:#3b3b3b;
  --charcoal-dark:#2e2e2e;
  --paper:#f2f1f1;
  --ink:#222;
  --muted:#555;
  --white:#fff;
}
*{box-sizing:border-box;margin:0;padding:0}
html,body{width:1200px;height:3930px;overflow:hidden}
body{position:relative;background:var(--paper);font-family:"Open Sans",Arial,sans-serif;color:var(--ink)}
.abs{position:absolute}

/* header */
.site-header{left:0;top:0;width:1200px;height:136px;background:var(--white)}
.brand{left:157px;top:28px;display:flex;align-items:center;gap:10px}
.brand-dot{width:26px;height:26px;border-radius:50%;background:var(--green)}
.brand-name{font-family:"Cinzel",serif;font-weight:700;font-size:30px;color:var(--green-dark);line-height:1}
.brand-sub{font-family:"Open Sans",sans-serif;font-size:10px;letter-spacing:2px;color:var(--green-dark);margin-top:4px}
.header-contact{right:175px;top:28px;display:flex;align-items:center;gap:14px;font-family:"Oswald",sans-serif;font-size:17px;color:var(--green)}
.social-dot{width:22px;height:22px;border-radius:50%;background:var(--green)}
.main-nav{left:612px;top:78px;display:flex;gap:30px;font-size:12px;color:#333}
.main-nav a{color:inherit;text-decoration:none;padding-bottom:8px}
.main-nav a.active{border-bottom:2px solid var(--green)}

/* hero */
.hero{left:0;top:136px;width:1200px;height:560px;background:linear-gradient(160deg,#4f7a3a 0%,#3f6a2a 35%,#8aa24a 55%,#b54a6a 75%,#5a7a2f 100%)}
.hero-title{left:162px;top:296px;font-family:"Cinzel",serif;font-size:30px;line-height:1.45;color:var(--white);letter-spacing:1px}
.btn{display:inline-block;border-radius:30px;font-size:11px;text-align:center;text-decoration:none}
.btn-green{background:var(--green);color:var(--white)}
.btn-ghost{border:2px solid var(--white);color:var(--white)}
.hero-btn{left:158px;top:408px;width:114px;height:34px;line-height:34px}
.slide-arrow{width:32px;height:32px;border-radius:50%;border:2px solid var(--white)}
.hero-wave{left:0;top:580px}

/* welcome */
.section-title{width:1200px;left:0;text-align:center;font-family:"Cinzel",serif;font-weight:700;font-size:28px;letter-spacing:1px;color:var(--ink)}
.welcome-block{left:170px;top:838px;width:350px;display:flex;flex-direction:column;align-items:flex-start}
.welcome-copy{font-size:10.5px;line-height:20px;color:#333}
.welcome-btn{margin-top:22px;width:114px;height:34px;line-height:34px}
.welcome-frame{left:568px;top:832px;width:358px;height:242px;border:2px solid var(--green)}
.welcome-photo{left:597px;top:860px;width:440px;height:240px;background:linear-gradient(150deg,#7ba04e,#4e8a2c 50%,#b7725a 100%)}

/* treatment panels */
.panel{top:1179px;width:400px;height:556px}
.panel-title{position:absolute;left:60px;top:52px;font-family:"Cinzel",serif;font-size:32px;line-height:1.15;color:var(--white)}
.panel-btn{position:absolute;left:58px;top:463px;width:138px;height:40px;line-height:36px}
.panel-1{left:0;background:linear-gradient(180deg,#5f7f44,#3e5a2c 60%,#2e4520)}
.panel-2{left:400px;background:linear-gradient(180deg,#4e6f2c,#9dc24f 50%,#3f7a23)}
.panel-3{left:800px;background:linear-gradient(180deg,#3b5a2a,#4f8a2a 50%,#2f5e1c)}

/* lawn treatments */
.treatments-copy{left:200px;top:1895px;width:800px;text-align:center;font-size:10.5px;line-height:2.5;color:#333}

/* call band */
.call-band{left:0;top:2100px;width:1200px;height:290px}
.call-text{left:60px;top:2200px;width:330px;text-align:right;font-family:"Oswald",sans-serif;color:var(--white)}
.call-text .k{font-size:24px;font-weight:500}
.call-text .n{font-size:44px;font-weight:500;line-height:1.2}
.call-text .s{font-size:22px}
.service{top:2210px;width:200px;text-align:center;font-family:"Cinzel",serif;font-size:18px;line-height:1.1;color:var(--white)}
.service svg{display:block;margin:0 auto 10px}

/* recent work */
.work-photo{top:2554px;width:281px;height:205px}
.work-1{left:144px;background:linear-gradient(150deg,#6a8a3a,#b55a7a 50%,#5a8a2f)}
.work-2{left:458px;background:linear-gradient(160deg,#3f6a2a,#7fbf3a 60%,#c04a3a)}
.work-3{left:773px;background:linear-gradient(160deg,#6b8a5a,#7fb04a 55%,#a06a4a)}
.round-arrow{width:40px;height:40px;border-radius:50%;background:var(--green)}
.view-more{left:527px;top:2800px;width:152px;height:46px;line-height:42px;border:2px solid #333;color:#333;font-size:12px;border-radius:30px}

/* analysis form */
.analysis{left:0;top:2908px;width:1200px;height:760px;background:radial-gradient(ellipse at 50% 40%,#5e9a2c,#2f5e16 80%)}
.analysis-title{top:2962px;color:var(--white)}
.field{background:var(--white);border-radius:30px;padding:0 26px;font-size:11px;color:#aaa;display:flex;align-items:center}
.field-msg{border-radius:26px;align-items:flex-start;padding-top:22px}
.submit{left:241px;top:3380px;width:718px;height:57px;line-height:57px;border-radius:30px;background:var(--green);color:var(--white);font-family:"Oswald",sans-serif;font-size:15px;text-align:center}

/* footer */
.site-footer{left:0;top:3560px;width:1200px;height:317px}
.footer-brand{left:147px;top:3620px;display:flex;align-items:center;gap:10px}
.footer-brand .brand-name{color:var(--white);font-size:28px}
.footer-copy{left:147px;top:3715px;width:240px;font-size:10.5px;line-height:1.9;color:#ddd}
.footer-social{left:147px;top:3800px;display:flex;gap:8px}
.footer-social span{width:20px;height:20px;border-radius:50%;background:#8a8a8a}
.footer-heading{font-family:"Cinzel",serif;font-size:15px;color:var(--white);letter-spacing:1px}
.footer-heading::after{content:"";display:block;width:30px;height:2px;background:var(--green);margin-top:8px}
.footer-map{left:438px;top:3668px;width:257px;height:153px;background:linear-gradient(135deg,#e8e6e0,#d6d9d2)}
.contact-list{left:812px;top:3660px;list-style:none;font-size:10.5px;color:#ddd}
.contact-list li{display:flex;align-items:center;gap:12px;height:44px}
.bottom-bar{left:0;top:3877px;width:1200px;height:53px;background:var(--green);color:var(--white);font-size:10.5px}
.bottom-bar .up{position:absolute;left:1048px;top:12px;width:28px;height:28px;border-radius:50%;background:var(--white)}
</style>
</head>
<body>

<header class="site-header abs">
  <div class="brand abs">
    <span class="brand-dot"></span>
    <div>
      <div class="brand-name">Brambleworth</div>
      <div class="brand-sub">LAWN CARE SERVICES</div>
    </div>
  </div>
  <div class="header-contact abs">
    <span class="social-dot"></span>
    <svg width="16" height="16" viewBox="0 0 24 24"><path d="M6.6 10.8a15 15 0 0 0 6.6 6.6l2.2-2.2a1 1 0 0 1 1-.25 11.4 11.4 0 0 0 3.6.57 1 1 0 0 1 1 1V20a1 1 0 0 1-1 1A17 17 0 0 1 3 4a1 1 0 0 1 1-1h3.5a1 1 0 0 1 1 1c0 1.25.2 2.45.57 3.57a1 1 0 0 1-.25 1z" fill="#9bcb3c"/></svg>
    <span>01632 960418</span>
  </div>
  <nav class="main-nav abs">
    <a class="active" href="#">Home</a><a href="#">Services</a><a href="#">Why Us</a><a href="#">Blog</a><a href="#">Portfolio</a><a href="#">Testimonials</a><a href="#">Contact</a>
  </nav>
</header>

<section class="hero abs" role="img" aria-label="Landscaped garden with colourful flower beds and a winding path"></section>
<h1 class="hero-title abs">Expert Lawn Treatment<br>Service</h1>
<a class="btn btn-green hero-btn abs" href="#">Our Services</a>
<span class="slide-arrow abs" style="left:44px;top:362px"></span>
<span class="slide-arrow abs" style="left:1116px;top:362px"></span>
<svg class="hero-wave abs" width="1200" height="120" viewBox="0 0 1200 120" preserveAspectRatio="none">
  <path d="M0 75 C250 120 520 60 760 30 C950 10 1100 40 1200 55 L1200 120 L0 120Z" fill="#a64599"/>
  <path d="M0 68 C240 110 520 60 760 40 C950 25 1100 55 1200 70 L1200 120 L0 120Z" fill="#9bcb3c"/>
  <path d="M0 85 C250 125 520 75 760 55 C950 40 1100 70 1200 82 L1200 120 L0 120Z" fill="#f2f1f1"/>
</svg>

<h2 class="section-title abs" style="top:738px">Welcome To Brambleworth Lawn Care</h2>
<div class="welcome-block abs">
  <p class="welcome-copy">As expert gardeners, we are passionate about horticulture and working to bring out the very best in your garden. When we work in your garden, we look at it and treat it with the same care and attention as if it were our own, before handing it back for you to enjoy. Our passion doesn't end with just trees and shrubs, though. Your grass is as much of a living, breathing plant as your shrubs and we, therefore, utilise our expert horticultural knowledge to ensure your lawn thrives and reaches its fullest potential.<br>Lawn care isn't just about applying a fertiliser.</p>
  <a class="btn btn-green welcome-btn" href="#">Learn More</a>
</div>
<div class="welcome-frame abs"></div>
<div class="welcome-photo abs" role="img" aria-label="Neatly edged garden lawn beside a brick path"></div>

<div class="panel panel-1 abs" role="img" aria-label="Red lawn spreader on a green lawn">
  <h3 class="panel-title">Spring<br>Treatment</h3>
  <a class="btn btn-ghost panel-btn" href="#">Learn More</a>
</div>
<div class="panel panel-2 abs" role="img" aria-label="Curving garden path through bright summer lawn">
  <h3 class="panel-title">Early Summer<br>Treatment</h3>
  <a class="btn btn-ghost panel-btn" href="#">Learn More</a>
</div>
<div class="panel panel-3 abs" role="img" aria-label="Lawn mower cutting striped grass">
  <h3 class="panel-title">Grow<br>Slow</h3>
  <a class="btn btn-ghost panel-btn" href="#">Learn More</a>
</div>

<h2 class="section-title abs" style="top:1832px">Lawn Treatments</h2>
<p class="treatments-copy abs">As gardeners and horticulturalists we knew what we wanted out of a lawn care product and so spent a great deal of time collaborating with a top agronomist and former premiership football sports turf consultant, to make sure we selected the very best fertilisers and treatments out there on the market. It will come as no surprise that our highly specialised, organic products are not available to the general public, as they are reserved for use by professionals on some of the most prestigious greens in the world. But now you can benefit from the same specialist treatments and couple with the expert horticultural knowledge of us at Brambleworth Gardening Services, create the healthiest, lushest and greenest of lawns.</p>

<svg class="call-band abs" width="1200" height="290" viewBox="0 0 1200 290">
  <rect x="0" y="40" width="1200" height="250" fill="#3b3b3b"/>
  <path d="M0 40 C150 10 320 0 453 40 L453 290 L0 290Z" fill="#a64599"/>
  <path d="M453 40 C700 -5 950 10 1200 45 L1200 60 C950 25 700 12 453 55Z" fill="#a64599"/>
  <rect x="0" y="60" width="453" height="230" fill="#a64599"/>
</svg>
<div class="call-text abs">
  <div class="k">CALL US TODAY</div>
  <div class="n">01632 960418</div>
  <div class="s">Same Day Service</div>
</div>
<div class="service abs" style="left:485px">
  <svg width="60" height="60" viewBox="0 0 60 60" fill="none" stroke="#9bcb3c" stroke-width="2.5"><circle cx="20" cy="24" r="13"/><circle cx="40" cy="22" r="14"/><path d="M20 37v16M40 36v17M6 53h48"/></svg>
  Landscape<br>Management
</div>
<div class="service abs" style="left:720px">
  <svg width="60" height="60" viewBox="0 0 60 60" fill="none" stroke="#9bcb3c" stroke-width="2.5"><circle cx="30" cy="14" r="8"/><path d="M30 22v14M30 30c-6-4-10-3-12 0M30 30c6-4 10-3 12 0M18 36h24l-4 18H22z"/></svg>
  Interior<br>Plantscaping
</div>
<div class="service abs" style="left:950px">
  <svg width="60" height="60" viewBox="0 0 60 60" fill="none" stroke="#9bcb3c" stroke-width="2.5"><path d="M30 6v48M9 18l42 24M9 42l42-24M24 10l6 6 6-6M24 50l6-6 6 6"/></svg>
  Snow &amp; Ice<br>Removal
</div>

<h2 class="section-title abs" style="top:2458px">Recent Work</h2>
<div class="work-photo work-1 abs" role="img" aria-label="Garden path lined with flower beds"></div>
<div class="work-photo work-2 abs" role="img" aria-label="Bright green lawn with red flower border"></div>
<div class="work-photo work-3 abs" role="img" aria-label="Lawn and brick paving by a garden fence"></div>
<svg class="round-arrow abs" style="left:51px;top:2636px" viewBox="0 0 40 40"><path d="M23 13l-7 7 7 7" stroke="#fff" stroke-width="3" fill="none"/></svg>
<svg class="round-arrow abs" style="left:1107px;top:2636px" viewBox="0 0 40 40"><path d="M17 13l7 7-7 7" stroke="#fff" stroke-width="3" fill="none"/></svg>
<a class="btn view-more abs" href="#">View More</a>

<section class="analysis abs" role="img" aria-label="Close-up of green lawn grass"></section>
<h2 class="section-title analysis-title abs">Lawn Care Analysis</h2>
<div class="field abs" style="left:241px;top:3060px;width:349px;height:58px">Name</div>
<div class="field abs" style="left:610px;top:3060px;width:349px;height:58px">Phone Number</div>
<div class="field abs" style="left:241px;top:3136px;width:349px;height:58px">Email</div>
<div class="field abs" style="left:610px;top:3136px;width:349px;height:58px">Postcode</div>
<div class="field field-msg abs" style="left:241px;top:3222px;width:718px;height:132px">Message</div>
<div class="submit abs">SUBMIT</div>

<svg class="site-footer abs" width="1200" height="317" viewBox="0 0 1200 317">
  <path d="M0 20 C300 70 650 30 900 15 C1050 6 1140 15 1200 25 L1200 317 L0 317Z" fill="#9bcb3c"/>
  <path d="M0 32 C300 80 650 40 900 28 C1050 20 1140 30 1200 38 L1200 317 L0 317Z" fill="#3b3b3b"/>
</svg>
<div class="footer-brand abs">
  <span class="brand-dot"></span>
  <span class="brand-name">Brambleworth</span>
</div>
<p class="footer-copy abs">Lorem Ipsum is simply dummy text of the printing and typesetting industry. Lorem Ipsum has been the industry's standard dummy text ever since the 1500s.</p>
<div class="footer-social abs"><span></span><span></span><span></span><span></span></div>
<div class="abs footer-heading" style="left:438px;top:3612px">Find Us Here</div>
<div class="footer-map abs" role="img" aria-label="Street map showing the business location"></div>
<div class="abs footer-heading" style="left:812px;top:3612px">Contact Us</div>
<ul class="contact-list abs">
  <li><svg width="14" height="16" viewBox="0 0 24 24"><path d="M12 2a7 7 0 0 0-7 7c0 5 7 13 7 13s7-8 7-13a7 7 0 0 0-7-7zm0 9.5A2.5 2.5 0 1 1 12 6a2.5 2.5 0 0 1 0 5.5z" fill="#fff"/></svg>Hostara Business Centre Orchard Close Milbrook MB2 4QL</li>
  <li><svg width="14" height="14" viewBox="0 0 24 24"><path d="M6.6 10.8a15 15 0 0 0 6.6 6.6l2.2-2.2a1 1 0 0 1 1-.25 11.4 11.4 0 0 0 3.6.57 1 1 0 0 1 1 1V20a1 1 0 0 1-1 1A17 17 0 0 1 3 4a1 1 0 0 1 1-1h3.5a1 1 0 0 1 1 1c0 1.25.2 2.45.57 3.57a1 1 0 0 1-.25 1z" fill="#fff"/></svg>01632 960418</li>
  <li><svg width="16" height="12" viewBox="0 0 24 18"><rect x="1" y="1" width="22" height="16" fill="none" stroke="#fff" stroke-width="2"/><path d="M1 1l11 9 11-9" fill="none" stroke="#fff" stroke-width="2"/></svg>enquiries@brambleworthlawns.co.uk</li>
</ul>
<div class="bottom-bar abs">
  <svg class="up" viewBox="0 0 28 28"><path d="M9 16l5-5 5 5" stroke="#333" stroke-width="2.5" fill="none"/></svg>
</div>

</body>
</html>
```